Lantern Business Cards

Need business cards for my employees at my restaurant.

Needs to include:
Our Logo
Lantern Bowls & Brews
Name: Nora Pettigrew
Title : Owner
Address: 487 Mirella Ave. Lake Havasu City, AZ 86519
Web: www.lanternkestrel.com
Phone: 928-555-0147
Cell: 928-555-0192
Email: info@lanternkestrel.com

```html
<!DOCTYPE html>
<html lang="en">
<head>
<meta charset="UTF-8">
<title>Lantern Bowls &amp; Brews – Business Card</title>
<link rel="stylesheet" href="https://fonts.googleapis.com/css2?family=Montserrat:wght@400;500;700&display=swap">
<style>
  :root {
    --backdrop: #2a2a2c;
    --card-white: #ffffff;
    --brand-red: #c12131;
    --ink: #1a1a1a;
    --ink-soft: #3a3a3a;
    --card-black: #0e0e0f;
    --pattern-grey: #3b3c3e;
  }
  * { box-sizing: border-box; margin: 0; padding: 0; }
  html, body { width: 1200px; height: 800px; overflow: hidden; }
  body {
    background: var(--backdrop);
    font-family: "Montserrat", sans-serif;
    display: flex;
    align-items: center;
    justify-content: center;
    gap: 40px;
  }
  .card {
    position: relative;
    width: 540px;
    height: 309px;
    border-radius: 16px;
    overflow: hidden;
  }
  .card-front { background: var(--card-white); }

  .brand-block {
    position: absolute;
    left: 34px;
    top: 78px;
    width: 190px;
    display: flex;
    align-items: center;
    gap: 10px;
  }
  .brand-mark {
    flex: none;
    width: 16px;
    height: 16px;
    border-radius: 50%;
    background: var(--brand-red);
  }
  .brand-name {
    color: var(--brand-red);
    font-weight: 700;
    font-size: 25px;
    line-height: 1.1;
    text-transform: uppercase;
  }

  .divider {
    position: absolute;
    left: 244px;
    top: 62px;
    width: 1.5px;
    height: 134px;
    background: var(--ink);
  }

  .person {
    position: absolute;
    left: 268px;
    top: 62px;
  }
  .person-name {
    color: var(--brand-red);
    font-weight: 700;
    font-size: 18px;
    letter-spacing: 0.3px;
    text-transform: uppercase;
  }
  .person-title {
    color: var(--ink);
    font-size: 14px;
    font-weight: 500;
    margin-top: 1px;
  }

  .contact-list {
    position: absolute;
    left: 268px;
    top: 118px;
    list-style: none;
  }
  .contact-item {
    display: flex;
    align-items: center;
    gap: 9px;
    color: var(--ink-soft);
    font-size: 13px;
    line-height: 19px;
  }
  .contact-icon { width: 12px; height: 12px; fill: var(--brand-red); flex: none; }

  .address-band {
    position: absolute;
    left: 0;
    top: 218px;
    width: 540px;
    height: 32px;
  }
  .address-text {
    position: absolute;
    left: 30px;
    top: 218px;
    height: 32px;
    line-height: 32px;
    color: var(--card-white);
    font-size: 14px;
    font-weight: 500;
    letter-spacing: 0.3px;
  }

  .card-back { background: var(--card-black); }
  .back-texture {
    position: absolute;
    inset: 0;
    background: radial-gradient(circle at 40% 35%, var(--pattern-grey), var(--card-black) 75%);
  }
  .back-brand {
    position: absolute;
    right: 70px;
    top: 130px;
    display: flex;
    align-items: center;
    gap: 9px;
  }
  .back-brand .brand-name { font-size: 22px; }
</style>
</head>
<body>
  <section class="card card-front" aria-label="Business card front">
    <div class="brand-block">
      <span class="brand-mark"></span>
      <span class="brand-name">Lantern Bowls &amp; Brews</span>
    </div>

    <div class="divider"></div>

    <div class="person">
      <p class="person-name">Nora Pettigrew</p>
      <p class="person-title">Owner</p>
    </div>

    <ul class="contact-list">
      <li class="contact-item">
        <svg class="contact-icon" viewBox="0 0 12 12"><path d="M1 4c0-2 10-2 10 0v1H8V4H4v1H1zM3 6h6l1 5H2z"/></svg>
        928-555-0147
      </li>
      <li class="contact-item">
        <svg class="contact-icon" viewBox="0 0 12 12"><path d="M3 0h6a1 1 0 0 1 1 1v10a1 1 0 0 1-1 1H3a1 1 0 0 1-1-1V1a1 1 0 0 1 1-1zm0 2v7h6V2z"/></svg>
        928-555-0192
      </li>
      <li class="contact-item">
        <svg class="contact-icon" viewBox="0 0 12 12"><path d="M0 2h12v1L6 7 0 3zm0 2.5l6 4 6-4V10H0z"/></svg>
        info@lanternkestrel.com
      </li>
      <li class="contact-item">
        <svg class="contact-icon" viewBox="0 0 12 12"><circle cx="6" cy="6" r="6"/></svg>
        www.lanternkestrel.com
      </li>
    </ul>

    <svg class="address-band" viewBox="0 0 540 32" preserveAspectRatio="none" aria-hidden="true">
      <polygon points="0,0 460,0 436,32 0,32" fill="var(--brand-red)"/>
      <polygon points="460,0 540,0 540,32 436,32" fill="var(--card-black)"/>
    </svg>
    <p class="address-text">487 Mirella Ave. Lake Havasu City, AZ 86519</p>
  </section>

  <section class="card card-back" aria-label="Business card back">
    <div class="back-texture" role="img" aria-label="Repeating embossed brand pattern in glossy black"></div>
    <div class="back-brand">
      <span class="brand-mark"></span>
      <span class="brand-name">Lantern</span>
    </div>
  </section>
</body>
</html>
```